For lease banners for Businesses

I need to turn all of these banners into high quality graphics so I can get them printed on vinyl vertical banners that are 44"W x 88"H. So I need them most likely to be vector artwork, and ready to upload to a custom vinyl print shop.

```html
<!DOCTYPE html>
<html lang="en">
<head>
<meta charset="utf-8">
<title>For Lease Banners</title>
<link rel="stylesheet" href="https://fonts.googleapis.com/css2?family=Bebas+Neue&family=Montserrat:wght@500&family=Roboto:wght@400;700&family=Yellowtail&display=swap">
<style>
  :root {
    --stage: #9b9c9e;
    --ink: #000000;
    --white: #ffffff;
    --gold: #c39035;
    --charcoal: #333333;
    --rule: #6a5a3a;
    --grey-text: #2f2f2f;
  }
  * { box-sizing: border-box; margin: 0; padding: 0; }
  html, body { width: 1200px; height: 882px; overflow: hidden; }
  body { background: var(--stage); position: relative; font-family: "Roboto", sans-serif; }

  .banner { position: absolute; width: 294px; height: 588px; overflow: hidden; }
  .banner--lease { left: 137px; top: 148px; background: var(--ink); }
  .banner--name { left: 444px; top: 147px; background: var(--white); }
  .banner--location { left: 768px; top: 146px; background: var(--ink); }

  .abs { position: absolute; }
  .center { left: 0; right: 0; text-align: center; }

  /* brand lockup */
  .brand { position: absolute; display: flex; align-items: center; gap: 12px; }
  .brand__mark { width: 42px; height: 46px; border: 1.5px solid var(--gold); }
  .brand__name {
    font-family: "Montserrat", sans-serif; font-weight: 500; color: var(--white);
    font-size: 17px; letter-spacing: 4px; line-height: 1.25;
  }

  /* banner 1 */
  .lease__brand { left: 53px; top: 15px; }
  .lease__rule { left: 13px; right: 13px; top: 77px; height: 1px; background: var(--rule); }
  .lease__photo {
    left: 0; right: 0; top: 215px; height: 325px;
    background:
      linear-gradient(180deg, #000 0%, rgba(0,0,0,0) 14%),
      radial-gradient(ellipse at 55% 68%, #c9893b 0%, #6b4323 30%, rgba(40,38,45,0) 62%),
      linear-gradient(180deg, #2a2c3a 0%, #4a4653 35%, #3a2c22 70%, #55524f 100%);
  }
  .lease__headline {
    font-family: "Bebas Neue", sans-serif; color: var(--white);
    font-size: 104px; line-height: 1; letter-spacing: 10px; padding-left: 10px;
  }
  .lease__for { top: 84px; }
  .lease__word { top: 163px; background: linear-gradient(180deg, #fff 55%, #dcdcee 100%); -webkit-background-clip: text; background-clip: text; color: transparent; }
  .lease__features { left: 0; right: 0; top: 390px; height: 80px; background: var(--ink); }
  .feature { position: absolute; top: 0; text-align: center; color: var(--white); font-weight: 700; font-size: 12.5px; line-height: 1.3; }
  .feature svg { display: block; margin: 6px auto 8px; }
  .divider-v { position: absolute; width: 1px; background: var(--gold); }
  .lease__rule2 { left: 15px; right: 10px; top: 466px; height: 1px; background: #555; }
  .lease__phone {
    top: 472px; font-family: "Bebas Neue", sans-serif; color: var(--white);
    font-size: 64px; line-height: 1; letter-spacing: 0;
  }
  .lease__diamond-line { left: 27px; right: 19px; top: 536px; height: 1px; background: #555; }
  .lease__diamond { left: 148px; top: 532px; width: 8px; height: 8px; background: var(--gold); transform: rotate(45deg); }
  .lease__email { top: 553px; color: var(--white); font-weight: 700; font-size: 16.5px; }
  .lease__band { left: 0; right: 0; bottom: 0; height: 8px; background: var(--gold); }

  /* banner 2 */
  .name__headline {
    left: 25px; top: 24px; font-family: "Bebas Neue", sans-serif; color: var(--charcoal);
    font-size: 72px; line-height: 0.86; letter-spacing: 1px;
  }
  .name__list { left: 17px; top: 256px; list-style: none; }
  .name__list li { display: flex; align-items: center; gap: 10px; height: 18px; font-size: 15px; color: var(--grey-text); letter-spacing: 0.3px; }
  .name__illustration {
    left: 0; right: 0; top: 290px; height: 166px;
    background: linear-gradient(160deg, #ffffff 0%, #ffffff 30%, #d8d8d8 55%, #9a9a9a 75%, #e9e9e9 100%);
  }
  .footer { left: 0; right: 0; bottom: 0; background: var(--ink); }
  .name__footer { height: 132px; }
  .footer__brand { left: 45px; top: 20px; }
  .footer__leasing {
    font-family: "Roboto", sans-serif; font-weight: 700; color: var(--gold); font-size: 21px; letter-spacing: 0.5px;
  }
  .footer__sep { width: 1px; height: 34px; background: var(--gold); }
  .footer__contact { color: var(--white); }
  .footer__phone { display: flex; align-items: center; gap: 4px; font-weight: 700; font-size: 13px; }
  .footer__email { display: flex; align-items: center; gap: 5px; font-size: 5.5px; margin-top: 3px; }
  .footer__uses { color: var(--white); font-weight: 700; font-size: 15px; letter-spacing: 0.2px; }

  /* banner 3 */
  .location__photo {
    left: 0; right: 0; top: 0; bottom: 0;
    background:
      linear-gradient(180deg, rgba(0,0,0,0) 70%, rgba(0,0,0,0.85) 86%, #000 100%),
      radial-gradient(ellipse at 50% 62%, #5a4636 0%, rgba(60,50,40,0) 55%),
      linear-gradient(180deg, #3b3f2d 0%, #4a4a3e 30%, #5f5c57 42%, #2d2823 65%, #1a1714 100%);
  }
  .location__headline {
    top: 24px; font-family: "Bebas Neue", sans-serif; color: var(--white);
    font-size: 45px; line-height: 0.98; letter-spacing: 0;
  }
  .location__rule { left: 53px; width: 218px; top: 161px; height: 1.5px; background: var(--gold); }
  .location__script {
    top: 164px; font-family: "Yellowtail", cursive; color: var(--gold); font-size: 20px; line-height: 1.15;
  }
  .location__features { left: 0; right: 0; top: 388px; }
  .location__feature { position: absolute; top: 0; width: 66px; text-align: center; color: var(--white); font-weight: 700; font-size: 9.5px; line-height: 1.25; }
  .location__feature svg { display: block; margin: 0 auto 8px; }
  .location__brand { left: 44px; top: 468px; }
</style>
</head>
<body>

  <!-- Banner 1: For Lease -->
  <section class="banner banner--lease">
    <div class="abs lease__photo" role="img" aria-label="Photo of a modern brick commercial building with glass storefronts lit warmly at dusk"></div>
    <div class="brand lease__brand">
      <span class="brand__mark"></span>
      <span class="brand__name">CRESTLINE<br>HOLDINGS</span>
    </div>
    <div class="abs lease__rule"></div>
    <div class="abs center lease__headline lease__for">FOR</div>
    <div class="abs center lease__headline lease__word">LEASE</div>

    <div class="abs lease__features">
      <div class="feature" style="left:0;width:122px;">
        <svg width="26" height="26" viewBox="0 0 26 26" fill="none" stroke="var(--gold)" stroke-width="1.3">
          <rect x="3" y="8" width="9" height="17"/><rect x="12" y="3" width="7" height="22"/><rect x="19" y="11" width="5" height="14"/>
          <path d="M5 11h2M8 11h2M5 14h2M8 14h2M5 17h2M8 17h2M14 7h3M14 10h3M14 13h3M14 16h3"/>
        </svg>
        COMMERCIAL<br>SPACE
      </div>
      <div class="divider-v" style="left:107px;top:8px;height:62px;"></div>
      <div class="feature" style="left:108px;width:98px;">
        <svg width="32" height="26" viewBox="0 0 32 26" fill="none" stroke="var(--gold)" stroke-width="1.3" stroke-linejoin="round">
          <path d="M2 8l6-4 6 3 4-2 6 1 6 3"/><path d="M8 4l-6 10 4 3"/><path d="M30 11l-5 6-8 6-3-2-3-3-3-2"/><path d="M14 7l-5 5 2 2 5-4 7 6"/>
        </svg>
        FLEXIBLE<br>OPPORTUNITY
      </div>
      <div class="divider-v" style="left:206px;top:8px;height:62px;"></div>
      <div class="feature" style="left:207px;width:87px;">
        <svg width="28" height="26" viewBox="0 0 28 26" fill="none" stroke="var(--gold)" stroke-width="1.3">
          <circle cx="14" cy="8" r="4"/><circle cx="6" cy="10" r="3"/><circle cx="22" cy="10" r="3"/>
          <path d="M7 24v-4a7 7 0 0 1 14 0v4z"/><path d="M2 22v-3a4 4 0 0 1 5-4"/><path d="M26 22v-3a4 4 0 0 0-5-4"/>
        </svg>
        LOCALLY<br>OWNED
      </div>
    </div>

    <div class="abs lease__rule2"></div>
    <div class="abs center lease__phone">555-014-2290</div>
    <div class="abs lease__diamond-line"></div>
    <div class="abs lease__diamond"></div>
    <div class="abs center lease__email">leasing@crestlineholdings.com</div>
    <div class="abs lease__band"></div>
  </section>

  <!-- Banner 2: Your Name Here -->
  <section class="banner banner--name">
    <div class="abs name__headline">YOUR<br>NAME<br>HERE</div>
    <div class="abs name__illustration" role="img" aria-label="Black and white illustration of a modern glass-front restaurant building with patio seating"></div>
    <ul class="abs name__list">
      <li><svg width="12" height="12" viewBox="0 0 12 12" fill="none" stroke="var(--gold)" stroke-width="1"><rect x="1.5" y="4" width="9" height="7.5"/><path d="M4 4V2.5a2 2 0 0 1 4 0V4"/></svg>RETAIL</li>
      <li><svg width="12" height="12" viewBox="0 0 12 12" fill="none" stroke="var(--gold)" stroke-width="1.1"><path d="M2 2l8 8M10 2L2 10"/></svg>RESTAURANT</li>
      <li><svg width="12" height="12" viewBox="0 0 12 12" fill="none" stroke="var(--gold)" stroke-width="1"><path d="M1 5h10l-1.5 6h-7z"/><path d="M4 5l2-3 2 3"/></svg>BOUTIQUE</li>
      <li><svg width="12" height="12" viewBox="0 0 12 12" fill="none" stroke="var(--gold)" stroke-width="1"><path d="M2 5h7v3a3 3 0 0 1-3 3H5a3 3 0 0 1-3-3z"/><path d="M9 6h1.5v2H9"/></svg>COFFEE OFFICE</li>
      <li style="display:none"></li>
    </ul>
    <div class="abs footer name__footer">
      <div class="brand footer__brand">
        <span class="brand__mark"></span>
        <span class="brand__name">CRESTLINE<br>HOLDINGS</span>
      </div>
      <div class="abs" style="left:17px;top:71px;display:flex;align-items:center;gap:8px;">
        <span class="footer__leasing">LEASING NOW</span>
        <span class="footer__sep"></span>
        <div class="footer__contact">
          <div class="footer__phone"><svg width="8" height="8" viewBox="0 0 10 10"><path d="M2 1l2 2-1 1.5a6 6 0 0 0 2.5 2.5L7 6l2 2-1.5 1.5C4 9 1 6 0.5 2.5z" fill="var(--gold)"/></svg>555-014-2290</div>
          <div class="footer__email"><svg width="8" height="6" viewBox="0 0 8 6"><rect width="8" height="6" fill="var(--gold)"/><path d="M0 0l4 3 4-3" stroke="#000" stroke-width="0.8" fill="none"/></svg>leasing@crestlineholdings.com</div>
        </div>
      </div>
      <div class="abs center footer__uses" style="top:106px;">RETAIL • RESTAURANT • OFFICE</div>
    </div>
  </section>

  <!-- Banner 3: Next Location -->
  <section class="banner banner--location">
    <div class="abs location__photo" role="img" aria-label="Photo of friends sharing a meal at an outdoor table on a busy downtown street under string lights"></div>
    <div class="abs center location__headline">THIS COULD BE<br>YOUR NEXT<br>LOCATION</div>
    <div class="abs location__rule"></div>
    <div class="abs center location__script">Build your business<br>where people gather</div>

    <div class="abs location__features">
      <div class="location__feature" style="left:19px;">
        <svg width="24" height="32" viewBox="0 0 24 32" fill="none" stroke="var(--gold)" stroke-width="1.5"><path d="M12 30S2 18 2 11a10 10 0 0 1 20 0c0 7-10 19-10 19z"/><circle cx="12" cy="11" r="4"/></svg>
        HIGH<br>VISIBILITY
      </div>
      <div class="location__feature" style="left:84px;">
        <svg width="36" height="30" viewBox="0 0 36 30" fill="none" stroke="var(--white)" stroke-width="1.4"><circle cx="18" cy="9" r="5"/><circle cx="8" cy="11" r="4"/><circle cx="28" cy="11" r="4"/><path d="M10 28v-5a8 8 0 0 1 16 0v5z"/><path d="M2 26v-3a6 6 0 0 1 6-6"/><path d="M34 26v-3a6 6 0 0 0-6-6"/></svg>
        DOWNTOWN<br>TRAFFIC
      </div>
      <div class="location__feature" style="left:150px;">
        <svg width="32" height="30" viewBox="0 0 32 30" fill="none" stroke="var(--white)" stroke-width="1.4"><rect x="10" y="1" width="12" height="8"/><rect x="2" y="19" width="12" height="10"/><rect x="18" y="19" width="12" height="10"/><path d="M16 9v5M8 19v-5h16v5"/></svg>
        FLEXIBLE<br>FLOORPLANS
      </div>
      <div class="location__feature" style="left:211px;top:-4px;">
        <svg width="38" height="30" viewBox="0 0 38 30" fill="none" stroke="var(--white)" stroke-width="1.4" stroke-linejoin="round"><path d="M2 10l7-5 7 3 5-2 7 1 8 4"/><path d="M9 5L2 16l4 3"/><path d="M36 11l-6 8-10 7-3-2-4-3-4-3"/><path d="M16 8l-6 6 2 2 6-4 9 7"/></svg>
        LOCAL<br>OWNERSHIP
      </div>
    </div>

    <div class="brand location__brand">
      <span class="brand__mark"></span>
      <span class="brand__name">CRESTLINE<br>HOLDINGS</span>
    </div>
    <div class="abs" style="left:17px;top:526px;display:flex;align-items:center;gap:8px;">
      <span class="footer__leasing">LEASING NOW</span>
      <span class="footer__sep"></span>
      <div class="footer__contact">
        <div class="footer__phone"><svg width="8" height="8" viewBox="0 0 10 10"><path d="M2 1l2 2-1 1.5a6 6 0 0 0 2.5 2.5L7 6l2 2-1.5 1.5C4 9 1 6 0.5 2.5z" fill="var(--gold)"/></svg>555-014-2290</div>
        <div class="footer__email"><svg width="8" height="6" viewBox="0 0 8 6"><rect width="8" height="6" fill="var(--gold)"/><path d="M0 0l4 3 4-3" stroke="#000" stroke-width="0.8" fill="none"/></svg>leasing@crestlineholdings.com</div>
      </div>
    </div>
    <div class="abs center footer__uses" style="top:554px;">RETAIL • RESTAURANT • OFFICE</div>
  </section>

</body>
</html>
```